Author needs a new book, Kindle and Audiobook cover design

I updated and re-edited a book I wrote 25 years ago but now realize the title and design did not get the job done. I am seeking a book, Kindle and audiobook design that will make me stand out. The final design will pop while being sensitive to the nature of the subject. The title of the book is Quiet Lanterns. Subtitle: Ways to Notice and Step Away From Harmful Circles While Keeping Steady Belief by Dorian T. Wexcombe. I am wanting to get the attention of people who have been damaged by a church relationship that started well but ended badly.
Updates

The book title is: Quiet Lanterns. The Subtitle is: Ways To Notice and Step Away From Harmful Circles While Keeping Steady Belief. The dimension is 6x9 (150 pages) and I am the author: Dorian T. Wexcombe

Target Market(s)

People with a church experience; church leadership. Religious abuse victims.

Industry/Entity Type

Christian

Font styles to use
Serif

Colors

Designer to choose colors to be used in the design.

Requirements
Nice to have
• I am not married to the Serif font if another design works better.

```html
<!DOCTYPE html>
<html lang="en">
<head>
<meta charset="utf-8">
<title>Quiet Lanterns – Back Cover</title>
<link rel="stylesheet" href="https://fonts.googleapis.com/css2?family=Open+Sans:wght@400;500&display=swap">
<style>
  :root {
    --page-bg: #d9d9d9;
    --gold-top: #f4d12b;
    --gold-mid: #d2b534;
    --olive: #6e6a3d;
    --slate: #2b3552;
    --navy: #13214a;
    --ink: #141414;
    --bio-gold: #f2cf45;
    --photo-frame: #6f7a3a;
  }
  * { box-sizing: border-box; margin: 0; padding: 0; }
  html, body {
    width: 1200px; height: 1200px; overflow: hidden;
    background: var(--page-bg);
  }
  .back-cover {
    position: absolute; left: 229px; top: 42px;
    width: 742px; height: 1116px; overflow: hidden;
    box-shadow: 0 4px 14px rgba(0,0,0,.25);
    font-family: "Open Sans", Arial, sans-serif;
    font-size: 17px; line-height: 24.5px; letter-spacing: .45px;
    color: var(--ink);
  }
  .cover-art {
    position: absolute; inset: 0;
    background:
      radial-gradient(ellipse 60% 40% at 55% 22%, rgba(255,240,150,.35), transparent 70%),
      linear-gradient(180deg, var(--gold-top) 0%, var(--gold-mid) 35%, #a8953a 48%, var(--olive) 60%, var(--slate) 76%, var(--navy) 90%, var(--navy) 100%);
  }
  .author-photo {
    position: absolute; left: 66px; top: 68px;
    width: 114px; height: 158px;
    border: 2px solid var(--photo-frame);
    background: linear-gradient(160deg, #2c3a55, #7a6a5c 55%, #2a3f7a);
  }
  .copy { position: absolute; text-align: justify; }
  .lead-quote { left: 198px; top: 74px; width: 488px; }
  .attrib-first { left: 67px; top: 263px; width: 619px; }
  .quote-two { left: 67px; top: 322px; width: 619px; }
  .quote-three { left: 69px; top: 511px; width: 617px; }
  .quote-four { left: 67px; top: 647px; width: 619px; }
  .author-bio {
    position: absolute; left: 70px; top: 929px; width: 602px;
    text-align: center; color: var(--bio-gold); font-weight: 500;
  }
</style>
</head>
<body>
  <div class="back-cover">
    <div class="cover-art" role="img" aria-label="Photo of a church with a cross rising against a golden sky, fading into a dark forest where a hooded person kneels in prayer"></div>
    <div class="author-photo" role="img" aria-label="Portrait photo of the author"></div>

    <p class="copy lead-quote">Dorian Wexcombe offers expert insight and a transparent evaluation in this book. With years of healthy involvement with that which is right in the body of Christ, he can speak to both the personal and systematic issues that cause bad environments to develop. The church landscape is littered with people who have been hurt in churches. This book will help clean things up</p>

    <p class="copy attrib-first">Milo Trentham, Senior Pastor, Cedar Hollow Fellowship, Alder Falls, VT. Cedarhollowfc.org “Seldom, if ever, have</p>

    <p class="copy quote-two">I read a book that was so refreshingly personal and real, yet delivered material that put you in a position to navigate the difficult and damaging challenges, of being part of a degenerating church. I was moved to tears and then lifted to a place of hope, by the pain and abuse that this family faced and their incredible testimony and journey of recovery. All glory to the power of His love for us.” -- RuthAnne, Kestrel Way Ministries, kestrelwayjourneys.com</p>

    <p class="copy quote-three">“Dorian Wexcombe offers a real-world view on how following your spiritual calling is not always easy but completely worth the journey. His down to earth approach allows the reader to process and be encouraged by his personal story, insight, and commitment to faith.” Lena Vostrikova, Executive Director, Wellspring Nine Ministry, Inc. Wellspring9.org</p>

    <p class="copy quote-four">“Dorian Wexcombe has been a pastor over 40 years. I have known him personally for many of those years. This book is a case study of how trust can be abused. Dorian handles this difficult issue with a good balance of honest introspection and critical analysis of leadership structures and practices. This book is a must-read.” -- Gareth L. Pemberly, ReasonedFaithNotes.com</p>

    <p class="author-bio">Dorian Wexcombe is a long-time pastor, author and podcaster who has impacted leaders and churches for many years. He wrote Harbor Warning, a study of church leadership drawn from the history of the legendary ship. He and his wife Marisol, together with their grown children and spouses all serve in ministry.</p>
  </div>
</body>
</html>
```